political election

Elect Mateo Quiroga

for

Brenwick School Board Pl. ?

colors used are red, white, and blue

any other graphics are more than welcome.

need this in fine print at bottom

advertising paid for by candidate

voters of the school district

School

• red white and blue and in fine print advertisement paid for by candidate.
• graphics, art

```html
<!DOCTYPE html>
<html lang="en">
<head>
<meta charset="utf-8">
<title>Elect Mateo Quiroga – Brenwick School Board</title>
<link rel="stylesheet" href="https://fonts.googleapis.com/css2?family=Figtree:wght@700;800;900&display=swap">
<style>
  :root {
    --page: #eef0f3;
    --navy: #1d4a86;
    --navy-shadow: #153a6c;
    --red: #d8402b;
    --white: #f1f2f4;
  }
  html, body {
    margin: 0;
    width: 1200px;
    height: 1000px;
    overflow: hidden;
    background: var(--page);
  }
  .canvas {
    position: relative;
    width: 1200px;
    height: 1000px;
  }
  .card {
    position: absolute;
    left: 60px;
    top: 140px;
    width: 1080px;
    height: 720px;
    background: var(--navy);
    border-radius: 6px;
    overflow: hidden;
    box-shadow: 0 10px 30px rgba(20, 40, 70, 0.18);
    font-family: "Figtree", "Helvetica Neue", Arial, sans-serif;
    color: var(--white);
  }
  .card-art {
    position: absolute;
    left: 0;
    top: 0;
    width: 360px;
    height: 720px;
    background:
      linear-gradient(90deg, rgba(29, 74, 134, 0) 55%, var(--navy) 100%),
      linear-gradient(160deg, var(--red) 0%, #b8433f 30%, #8f5a86 55%, var(--white) 80%, #9fb2cc 100%);
    opacity: 0.9;
  }
  .headline {
    position: absolute;
    left: 376px;
    top: 104px;
    margin: 0;
    font-weight: 900;
    line-height: 1;
    text-shadow: 6px 8px 0 var(--navy-shadow);
  }
  .headline-elect {
    display: block;
    font-size: 56px;
    font-weight: 800;
    margin-bottom: 4px;
  }
  .headline-name {
    display: block;
    font-size: 136px;
    letter-spacing: -2px;
    line-height: 0.95;
  }
  .headline-for {
    font-size: 50px;
    font-weight: 800;
    letter-spacing: 0;
    margin-left: 12px;
  }
  .headline-office {
    display: block;
    font-size: 72px;
    font-weight: 800;
    line-height: 1.12;
    margin-top: 16px;
  }
  .disclaimer {
    position: absolute;
    right: 38px;
    bottom: 30px;
    margin: 0;
    font-size: 16px;
    font-weight: 700;
    letter-spacing: 0.3px;
  }
</style>
</head>
<body>
<main class="canvas">
  <article class="card">
    <div class="card-art" role="img" aria-label="Patriotic artwork of white stars and sweeping red ribbons"></div>

    <h1 class="headline">
      <span class="headline-elect">Elect</span>
      <span class="headline-name">Mateo</span>
      <span class="headline-name">Quiroga<span class="headline-for">for</span></span>
      <span class="headline-office">Brenwick School<br>Board Pl.</span>
    </h1>

    <p class="disclaimer">advertising paid for by candidate***</p>
  </article>
</main>
</body>
</html>
```